Talvick Industrial Maintenance Business Card

Design a business card with the following information, logo must be included.
Talvick Industrial Maintenance
Dan Pelfrey Jr.
Pone 555-214-7608
email dan.pelfrey.jr@mailvantor.com

```html
<!DOCTYPE html>
<html lang="en">
<head>
<meta charset="utf-8">
<title>Talvick Industrial Maintenance – Business Card</title>
<link rel="stylesheet" href="https://fonts.googleapis.com/css2?family=Montserrat:wght@500;600;700&display=swap">
<style>
  :root {
    --backdrop: #3b3b3b;
    --card: #141414;
    --card-deep: #0c0c0c;
    --brand-blue: #1a74c4;
    --edge-blue: #1f7fd6;
    --text-light: #e6e6e6;
    --mark-tone: #1d1d1d;
    --mark-sheen: #2a2a2a;
  }
  * { box-sizing: border-box; margin: 0; padding: 0; }
  html, body { width: 1200px; height: 801px; overflow: hidden; }
  body {
    background: var(--backdrop);
    font-family: "Montserrat", Arial, sans-serif;
    position: relative;
  }
  .card {
    position: absolute;
    top: 250px;
    width: 525px;
    height: 300px;
    background: var(--card);
    border: 2px solid var(--edge-blue);
    overflow: hidden;
  }
  .card--front { left: 50px; }
  .card--back { left: 625px; }

  .decor-circle {
    position: absolute;
    border-radius: 50%;
    background: radial-gradient(circle at 35% 30%, var(--mark-sheen), var(--mark-tone) 60%, var(--card-deep));
  }
  .card--front .decor-circle { width: 250px; height: 250px; right: -30px; top: -40px; }
  .card--back .decor-circle { width: 260px; height: 260px; left: -40px; top: 40px; }

  .brand {
    position: absolute;
    display: flex;
    align-items: center;
    gap: 10px;
  }
  .brand__dot {
    width: 34px; height: 34px;
    border-radius: 50%;
    background: var(--brand-blue);
    flex: none;
  }
  .brand__name {
    color: var(--brand-blue);
    font-weight: 600;
    text-transform: uppercase;
    line-height: 1.1;
  }
  .card--front .brand { left: 34px; top: 46px; }
  .card--front .brand__name { font-size: 17px; }
  .card--back .brand { left: 250px; top: 110px; }
  .card--back .brand__name { font-size: 22px; }
  .brand__line { display: block; }

  .person {
    position: absolute;
    left: 34px;
    top: 150px;
    color: var(--brand-blue);
    font-weight: 700;
    font-size: 17px;
    text-transform: uppercase;
    letter-spacing: 0.3px;
  }
  .contact {
    position: absolute;
    left: 34px;
    top: 196px;
    list-style: none;
    color: var(--text-light);
    font-size: 14px;
    font-weight: 500;
  }
  .contact li { display: flex; align-items: center; gap: 8px; margin-bottom: 8px; }
  .contact svg { width: 12px; height: 12px; fill: var(--brand-blue); flex: none; }
</style>
</head>
<body>
  <section class="card card--front">
    <div class="decor-circle" role="img" aria-label="Large glossy brand emblem decoration"></div>
    <div class="brand">
      <span class="brand__dot"></span>
      <span class="brand__name"><span class="brand__line">Talvick</span><span class="brand__line">Industrial Maintenance</span></span>
    </div>
    <p class="person">Dan Pelfrey Jr.</p>
    <ul class="contact">
      <li>
        <svg viewBox="0 0 24 24"><path d="M6.6 10.8a15.1 15.1 0 0 0 6.6 6.6l2.2-2.2a1 1 0 0 1 1-.25 11.4 11.4 0 0 0 3.6.57 1 1 0 0 1 1 1V20a1 1 0 0 1-1 1A17 17 0 0 1 3 4a1 1 0 0 1 1-1h3.5a1 1 0 0 1 1 1c0 1.25.2 2.45.57 3.57a1 1 0 0 1-.25 1z"/></svg>
        <span>555-214-7608</span>
      </li>
      <li>
        <svg viewBox="0 0 24 24"><path d="M2 5h20v14H2z M2 5l10 8 10-8" fill="none" stroke="var(--brand-blue)" stroke-width="2.5"/><path d="M2 5h20l-10 8z"/></svg>
        <span>dan.pelfrey.jr@mailvantor.com</span>
      </li>
    </ul>
  </section>

  <section class="card card--back">
    <div class="decor-circle" role="img" aria-label="Large glossy brand emblem decoration"></div>
    <div class="brand">
      <span class="brand__name"><span class="brand__line">Talvick</span><span class="brand__line">Industrial Maintenance</span></span>
    </div>
  </section>
</body>
</html>
```